Vornel Technologies business card design

We need a business card designed with our new logo. it would be great if the card could communicate it is a technology based company.

Target Market(s)

system integrators

Industry/Entity Type

technology, IOT

Contact Information for Business Card

Name, designation, Address, telephone number, email address

Requirements
Must have
• logo and company name
Nice to have
• something to do with technology

```html
<!DOCTYPE html>
<html lang="en">
<head>
<meta charset="utf-8">
<title>Vornel Technologies – Business Card</title>
<link rel="stylesheet" href="https://fonts.googleapis.com/css2?family=Open+Sans:wght@400;700&display=swap">
<style>
  :root {
    --orange: #f28a1e;
    --charcoal: #3a3a3a;
    --ink: #333333;
    --muted: #6b6b6b;
    --paper: #ffffff;
    --slate: #3b3b3c;
    --backdrop: #f2f2f2;
    --icon-grey: #a8a8a8;
  }
  * { box-sizing: border-box; margin: 0; padding: 0; }
  html, body { width: 1200px; height: 873px; overflow: hidden; }
  body {
    background: var(--backdrop);
    font-family: "Open Sans", Arial, sans-serif;
    display: flex;
    align-items: center;
    justify-content: center;
    gap: 40px;
  }
  .card {
    width: 540px;
    height: 310px;
    position: relative;
    overflow: hidden;
    box-shadow: 0 6px 18px rgba(0,0,0,0.15);
  }

  /* ---------- front ---------- */
  .card-front { background: var(--paper); color: var(--ink); }
  .contact-tab {
    position: absolute; left: 0; top: 0;
    width: 205px; height: 40px;
    background: var(--orange);
    border-bottom-right-radius: 14px;
    display: flex; align-items: center; justify-content: flex-end;
    gap: 8px; padding-right: 16px;
  }
  .contact-tab .tab-icon {
    width: 22px; height: 22px; border-radius: 50%;
    background: var(--paper);
    display: flex; align-items: center; justify-content: center;
  }
  .wave-band {
    position: absolute; left: 0; bottom: 0;
    width: 300px; height: 120px;
    background: linear-gradient(180deg, rgba(242,138,30,0) 0%, rgba(242,138,30,0.14) 55%, rgba(242,138,30,0.22) 100%);
  }
  .contact-list {
    position: absolute; left: 24px; top: 58px;
    list-style: none;
    font-size: 11.5px; line-height: 21px; color: var(--muted);
  }
  .divider {
    position: absolute; left: 232px; top: 62px;
    width: 1px; height: 150px; background: var(--charcoal);
  }
  .brand {
    position: absolute; left: 252px; top: 58px;
    display: flex; align-items: center; gap: 10px;
  }
  .brand-square { width: 26px; height: 26px; background: var(--orange); }
  .brand-name {
    font-size: 22px; font-weight: 700; color: var(--charcoal);
    letter-spacing: 0.5px; text-transform: uppercase; line-height: 1.05;
  }
  .person {
    position: absolute; left: 252px; top: 132px;
  }
  .person-name { font-size: 19px; font-weight: 700; color: var(--charcoal); letter-spacing: 0.5px; }
  .person-title { font-size: 14px; color: var(--orange); margin-top: 2px; }
  .social-row {
    position: absolute; left: 252px; top: 196px;
    display: flex; gap: 12px;
  }
  .social-square {
    width: 26px; height: 26px; border-radius: 6px;
    background: linear-gradient(180deg, #c4c4c4, #8e8e8e);
  }
  .address {
    position: absolute; left: 24px; right: 24px; bottom: 18px;
    font-size: 11.5px; color: var(--ink);
  }

  /* ---------- back ---------- */
  .card-back { background: var(--slate); }
  .card-back .brand {
    left: 50%; top: 50%; transform: translate(-50%, -60%);
    gap: 14px;
  }
  .card-back .brand-square { width: 34px; height: 34px; }
  .card-back .brand-name { color: var(--paper); font-size: 30px; }
  .social-tab {
    position: absolute; right: 0; bottom: 0;
    width: 190px; height: 44px;
    background: var(--orange);
    border-top-left-radius: 14px;
    display: flex; align-items: center; justify-content: center; gap: 10px;
  }
  .social-tab .social-square { width: 24px; height: 24px; }
</style>
</head>
<body>

<section class="card card-front" aria-label="Business card front">
  <div class="contact-tab">
    <span class="tab-icon">
      <svg width="12" height="12" viewBox="0 0 12 12"><circle cx="6" cy="6" r="4.5" fill="none" stroke="#3a3a3a" stroke-width="1.3"/><path d="M1.5 6h9M6 1.5c-2 2.5-2 6.5 0 9M6 1.5c2 2.5 2 6.5 0 9" fill="none" stroke="#3a3a3a" stroke-width="1"/></svg>
    </span>
    <span class="tab-icon">
      <svg width="12" height="12" viewBox="0 0 12 12"><path d="M3 1.5l1.8 2.3-1 1.2c.6 1.3 1.6 2.3 2.9 2.9l1.2-1 2.3 1.8-1 1.8C5.5 10.2 1.8 6.5 1.2 2.5z" fill="#3a3a3a"/></svg>
    </span>
    <span class="tab-icon">
      <svg width="12" height="12" viewBox="0 0 12 12"><path d="M6 1a3.5 3.5 0 0 0-3.5 3.5C2.5 7.5 6 11 6 11s3.5-3.5 3.5-6.5A3.5 3.5 0 0 0 6 1z" fill="#3a3a3a"/><circle cx="6" cy="4.5" r="1.3" fill="#fff"/></svg>
    </span>
    <span class="tab-icon">
      <svg width="12" height="12" viewBox="0 0 12 12"><rect x="1.5" y="3" width="9" height="6.5" fill="none" stroke="#3a3a3a" stroke-width="1.2"/><path d="M1.5 3.2L6 6.8l4.5-3.6" fill="none" stroke="#3a3a3a" stroke-width="1.2"/></svg>
    </span>
  </div>

  <div class="wave-band" role="img" aria-label="Soft orange flowing line pattern"></div>

  <ul class="contact-list">
    <li>info@vornel.com.au</li>
    <li>+61 400 555 019</li>
    <li>+61 400 555 019</li>
    <li>www.vornel.com.au</li>
  </ul>

  <div class="divider"></div>

  <div class="brand">
    <span class="brand-square"></span>
    <span class="brand-name">Vornel<br>Technologies</span>
  </div>

  <div class="person">
    <p class="person-name">MARCUS DELANEY</p>
    <p class="person-title">Executive Director</p>
  </div>

  <div class="social-row" aria-label="Social links">
    <span class="social-square"></span>
    <span class="social-square"></span>
    <span class="social-square"></span>
    <span class="social-square"></span>
  </div>

  <p class="address">Address: Suite 4, 21 Harlow Street, Marden ACT 2900 &nbsp;ABN: 47 219 835 604</p>
</section>

<section class="card card-back" aria-label="Business card back">
  <div class="brand">
    <span class="brand-square"></span>
    <span class="brand-name">Vornel<br>Technologies</span>
  </div>
  <div class="social-tab" aria-label="Social links">
    <span class="social-square"></span>
    <span class="social-square"></span>
    <span class="social-square"></span>
    <span class="social-square"></span>
  </div>
</section>

</body>
</html>
```